Book cover for publishing doctoral research about various national styles of piano playing.

I need a book cover for a publication of a doctoral research with regard to styles of piano performance characteristic to various nations.

Any images or graphics are optional, typography seems most important, but please feel free to be creative.

I attach the barcode, qsr and publisher's logo in the next few days. (Logo is still being designed).

For various reasons the size of the book is not completely decided yet. Please create your design in 7" x 10", but if at all possible, I would like to ask for files of two sizes, also including 8.5" x 11" in the final submission.

I am looking for a design that looks professional, probably simple, but I am open to any suggestions.

Dear Designers,I would like to thank you all for participation and submitting so many high-quality designs.My final decision was based on the feedback I received from my professional colleagues and potential readers.I would like to wish you all the best for the future.Best wishes,Tadeusz Added Monday, December 21, 2015

Pianists, students, music professionals

Publishing

• Title: Unfolding Seven Harbour Lullabies
• Subtitle: Memories and departures
• Author: Tadeusz Jarocki
• Space for my logo on the front page and the spine.
• On the back page, please include some space for a short biography, 'barcode' and 'qsr' code.
• Please include whatever else you consider necessary.
• Would it be possible to use the same cover to a e-book edition?

```html
<!DOCTYPE html>
<html lang="en">
<head>
<meta charset="utf-8">
<title>Unfolding Seven Harbour Lullabies — Cover Set</title>
<link rel="stylesheet" href="https://fonts.googleapis.com/css2?family=Oswald:wght@300;400;500&family=Open+Sans:wght@400&display=swap">
<style>
  :root {
    --ink: #231f20;
    --paper: #ffffff;
    --crimson: #8c000c;
    --pine: #004540;
    --tan: #ab7c57;
    --tan-light: #c4976a;
    --rule: #9a9697;
    --text-light: #ffffff;
  }
  * { margin: 0; padding: 0; box-sizing: border-box; }
  html, body { width: 1200px; height: 1200px; overflow: hidden; background: var(--paper); }
  .canvas { position: relative; width: 1200px; height: 1200px; background: var(--paper); font-family: "Oswald", sans-serif; }

  .cover { position: absolute; width: 327px; height: 470px; }
  .cover.front { top: 129px; }
  .cover.back { top: 618px; }
  .col-1 { left: 18px; }
  .col-2 { left: 364px; }
  .col-3 { left: 710px; }
  .crimson { background: var(--crimson); }
  .pine { background: var(--pine); }
  .tan { background: var(--tan); }

  .placeholder {
    position: absolute; width: 50px; height: 50px; background: var(--ink);
    color: var(--text-light); font-family: "Open Sans", sans-serif; font-size: 5.5px;
    display: flex; flex-direction: column; align-items: center; justify-content: center;
    gap: 9px; text-align: center; line-height: 1;
  }
  .cover .slot-top-left { left: 34px; top: 23px; }
  .cover .slot-top-right { left: 242px; top: 25px; }
  .cover .slot-bottom-left { left: 34px; top: 392px; }
  .cover .slot-bottom-right { left: 242px; top: 394px; }

  .instrument {
    position: absolute; left: 71px; top: 103px; width: 185px; height: 235px;
    background: var(--ink); border-radius: 70px 70px 0 0;
  }
  .title {
    position: absolute; left: 83px; top: 182px; width: 165px;
    color: var(--text-light); font-weight: 300; text-transform: uppercase; line-height: 0.92;
    white-space: nowrap;
  }
  .title .line-lg { display: block; font-size: 34px; }
  .title .line-sm { display: block; font-size: 20px; margin-top: 3px; letter-spacing: -0.2px; }
  .title-rule { position: absolute; left: 83px; top: 281px; width: 148px; height: 1px; background: var(--rule); }
  .subtitle {
    position: absolute; left: 83px; top: 286px; color: var(--text-light); font-weight: 400;
    font-size: 12.5px; line-height: 1.2; text-transform: uppercase; letter-spacing: -0.2px; white-space: nowrap;
  }
  .author-band {
    position: absolute; left: 71px; top: 341px; width: 185px; height: 28px; background: var(--ink);
    color: var(--text-light); font-weight: 300; font-size: 22px; line-height: 28px; text-align: center; text-transform: uppercase;
  }
  .bio { position: absolute; left: 106px; top: 244px; color: var(--text-light); font-family: "Open Sans", sans-serif; font-size: 7px; }

  .spine { position: absolute; width: 55px; }
  .spine.crimson-spine { left: 1060px; top: 129px; height: 468px; background: var(--crimson); }
  .spine.pine-spine { left: 1134px; top: 129px; height: 468px; background: var(--pine); }
  .spine.tan-spine { left: 1095px; top: 620px; height: 469px; width: 56px; background: var(--tan-light); }
  .spine .placeholder { left: 3px; width: 51px; }
  .spine .slot-top { top: 8px; }
  .spine .slot-bottom { top: 410px; }
  .spine-title, .spine-author {
    position: absolute; left: 50%; transform: translateX(-50%); writing-mode: vertical-rl;
    color: var(--text-light); text-transform: uppercase; white-space: nowrap;
  }
  .spine-title { top: 81px; font-size: 14px; font-weight: 400; letter-spacing: -0.3px; }
  .spine-author { top: 311px; font-size: 9.5px; font-weight: 300; opacity: 0.75; }
</style>
</head>
<body>
<main class="canvas">

  <section class="cover front col-1 crimson">
    <div class="placeholder slot-top-left"><span>LOGO</span></div>
    <div class="placeholder slot-top-right"><span>PUBLISHER</span><span>LOGO</span></div>
    <div class="instrument" role="img" aria-label="Dark grand piano silhouette seen from above"></div>
    <h1 class="title"><span class="line-lg">Unfolding</span><span class="line-lg">Seven</span><span class="line-sm">Harbour Lullabies</span></h1>
    <div class="title-rule"></div>
    <p class="subtitle">Memories and departures</p>
    <p class="author-band">Tadeusz Jarocki</p>
  </section>

  <section class="cover front col-2 pine">
    <div class="placeholder slot-top-left"><span>LOGO</span></div>
    <div class="placeholder slot-top-right"><span>PUBLISHER</span><span>LOGO</span></div>
    <div class="instrument" role="img" aria-label="Dark grand piano silhouette seen from above"></div>
    <h1 class="title"><span class="line-lg">Unfolding</span><span class="line-lg">Seven</span><span class="line-sm">Harbour Lullabies</span></h1>
    <div class="title-rule"></div>
    <p class="subtitle">Memories and departures</p>
    <p class="author-band">Tadeusz Jarocki</p>
  </section>

  <section class="cover front col-3 tan">
    <div class="placeholder slot-top-left"><span>LOGO</span></div>
    <div class="placeholder slot-top-right"><span>PUBLISHER</span><span>LOGO</span></div>
    <div class="instrument" role="img" aria-label="Dark grand piano silhouette seen from above"></div>
    <h1 class="title"><span class="line-lg">Unfolding</span><span class="line-lg">Seven</span><span class="line-sm">Harbour Lullabies</span></h1>
    <div class="title-rule"></div>
    <p class="subtitle">Memories and departures</p>
    <p class="author-band">Tadeusz Jarocki</p>
  </section>

  <aside class="spine crimson-spine">
    <div class="placeholder slot-top"><span>LOGO</span></div>
    <p class="spine-title">Unfolding Seven Harbour Lullabies</p>
    <p class="spine-author">Tadeusz Jarocki</p>
    <div class="placeholder slot-bottom"><span>PUBLISHER</span><span>LOGO</span></div>
  </aside>

  <aside class="spine pine-spine">
    <div class="placeholder slot-top"><span>LOGO</span></div>
    <p class="spine-title">Unfolding Seven Harbour Lullabies</p>
    <p class="spine-author">Tadeusz Jarocki</p>
    <div class="placeholder slot-bottom"><span>PUBLISHER</span><span>LOGO</span></div>
  </aside>

  <section class="cover back col-1 crimson">
    <div class="instrument" role="img" aria-label="Dark grand piano silhouette seen from above"></div>
    <p class="bio">(description biography)</p>
    <p class="author-band">Tadeusz Jarocki</p>
    <div class="placeholder slot-bottom-left"><span>BARCODE</span></div>
    <div class="placeholder slot-bottom-right"><span>QSR</span><span>CODE</span></div>
  </section>

  <section class="cover back col-2 pine">
    <div class="instrument" role="img" aria-label="Dark grand piano silhouette seen from above"></div>
    <p class="bio">(description biography)</p>
    <p class="author-band">Tadeusz Jarocki</p>
    <div class="placeholder slot-bottom-left"><span>BARCODE</span></div>
    <div class="placeholder slot-bottom-right"><span>QSR</span><span>CODE</span></div>
  </section>

  <section class="cover back col-3 tan">
    <div class="instrument" role="img" aria-label="Dark grand piano silhouette seen from above"></div>
    <p class="bio">(description biography)</p>
    <p class="author-band">Tadeusz Jarocki</p>
    <div class="placeholder slot-bottom-left"><span>BARCODE</span></div>
    <div class="placeholder slot-bottom-right"><span>QSR</span><span>CODE</span></div>
  </section>

  <aside class="spine tan-spine">
    <div class="placeholder slot-top"><span>LOGO</span></div>
    <p class="spine-title">Unfolding Seven Harbour Lullabies</p>
    <p class="spine-author">Tadeusz Jarocki</p>
    <div class="placeholder slot-bottom"><span>PUBLISHER</span><span>LOGO</span></div>
  </aside>

</main>
</body>
</html>
```